Wordpress Powered Website. Outstanding Design Required. Using Morvento Theme

Designers will not need to create anything other than the home page but there are some design elements on the home page which also need to be factored in: 6 product place holders and 2-3 slides for a slideshow (with images I provide).

Designers will need to familiarise themselves with the Morvento theme to make sure that their design will work within the theme.

The winning designer will set up all the pages and navigation in place. This includes social media icons, favicon, widgets, etc. In other words, the home page needs to be designed and coded and the other preset theme pages need to be organised in a way that we can start using the website on completion of the job.

Most of the designs I had last time were too colourful. This needs to be subtle not in your face.

Background to the business/website:
Tallow Banners is a new Australian venture which will sell large format printed banners and other signage. The market is very competitive so it is important to stand out visually and to have a website which is clean, easy to navigate and easy to order. It will be a combination of online sales and assisted sales but all sales enquiries will come from the website.

As our business is focused on presentation it is vital to have excellent design.
Purchased theme is Morvento. Only this theme is to be used.

1. A home page using all the preset features of the Morvento theme - it will just be basically taking my wireframe and inputting it to the live theme.
2. A three slide slideshow, ideally with an edited video. The static image slides can be provided by me during the handover. Placeholder for now.
Similar to this one: http://thebrindlework.com.au/

Attached is the logo which must be utilised, although it could also sit on a dark background. There is our mascot as well which can be used but does not have to be included.

Target Market(s)

Primarily B2B (business to business)
Main industries will be Construction, Retail, Community, Events & Trade Shows

Industry/Entity Type

Printing

Coding

Coded - Design and coding required

Font styles to use
Sans Serif

Requirements
Must have
• Must have the design files made to web pages within the Wordpress environment.
Nice to have
• Clean design. Stand out from competitors based on design.
Should not have
• Should not look like any competitor

```html
<!DOCTYPE html>
<html lang="en">
<head>
<meta charset="utf-8">
<title>Tallow Banners</title>
<link rel="stylesheet" href="https://fonts.googleapis.com/css2?family=Montserrat:wght@400;500;600;700&family=Open+Sans:ital,wght@0,400;0,600;1,400;1,600;1,700&display=swap">
<style>
:root{
  --blue:#1570c8;
  --blue-dark:#0f5ea8;
  --ink:#2a2a2a;
  --text:#444;
  --muted:#666;
  --light:#f3f3f3;
  --topbar:#161616;
  --footer:#1c1c1c;
  --green:#5e9a22;
  --yellow:#f5e10a;
  --white:#fff;
}
*{box-sizing:border-box;margin:0;padding:0}
html,body{width:1200px;height:2711px;overflow:hidden}
body{font-family:"Open Sans",Arial,sans-serif;color:var(--text);background:var(--white);position:relative}
.abs{position:absolute}
h2,h3,.nav a,.btn{font-family:"Montserrat",Arial,sans-serif}

/* top bar */
.topbar{left:0;top:0;width:1200px;height:36px;background:var(--topbar);color:var(--white);font-size:15px;font-weight:600}
.social{display:flex;gap:14px;position:absolute;top:11px}
.social span{width:13px;height:13px;border-radius:50%;background:var(--white);display:block}
.topbar .social{left:98px}
.contact-top{position:absolute;right:98px;top:8px;display:flex;gap:28px;align-items:center}
.contact-top span{display:flex;gap:8px;align-items:center}

/* header */
.header{left:0;top:36px;width:1200px;height:84px;background:var(--white)}
.brand{position:absolute;left:98px;top:20px;display:flex;align-items:center;gap:10px;font-family:"Montserrat",sans-serif;font-weight:700;font-size:28px;color:var(--blue)}
.brand i{width:34px;height:34px;background:var(--blue);display:block}
.nav{position:absolute;left:506px;top:26px;display:flex;align-items:center}
.nav a{font-size:14px;font-weight:500;color:var(--ink);text-decoration:none;padding:0 26px;border-left:1px solid #ccc;line-height:16px}
.nav a:nth-child(2){border-left:0}
.nav a.active{background:var(--blue);color:var(--white);padding:10px 16px;border:0;margin-right:10px}

/* hero */
.hero{left:0;top:120px;width:1200px;height:428px;background:linear-gradient(100deg,#5a4a3a 0%,#7a6b55 40%,#9b8f78 70%,#b2a58f 100%)}
.hero h1{position:absolute;left:100px;top:146px;width:500px;font-family:"Montserrat",sans-serif;font-weight:600;font-size:23px;line-height:34px;color:var(--white);text-shadow:0 1px 3px rgba(0,0,0,.5)}
.btn-yellow{position:absolute;left:100px;top:266px;background:var(--yellow);color:#222;font-size:15px;font-weight:600;padding:7px 16px;border-radius:3px;font-family:"Montserrat",sans-serif}
.circ{position:absolute;border-radius:50%;border:4px solid var(--white)}
.hero-brand{position:absolute;left:832px;top:162px;width:98px;height:98px;border-radius:50%;background:var(--white);display:flex;align-items:center;justify-content:center;font-family:"Montserrat",sans-serif;font-weight:700;font-size:13px;color:var(--blue);text-align:center;line-height:15px}
.dots{position:absolute;left:100px;top:396px;display:flex;gap:10px}
.dots span{width:13px;height:13px;border-radius:50%;border:2px solid var(--white)}
.dots span.on{background:var(--blue)}

/* section titles */
.title{position:absolute;left:0;width:1200px;text-align:center;font-family:"Montserrat",sans-serif;font-weight:600;font-size:25px;color:var(--ink);letter-spacing:.5px}
.title b{color:var(--blue);font-weight:600}
.rule{position:absolute;left:360px;width:480px;height:1px;background:#ddd}
.btn{display:inline-block;border:2px solid var(--blue);color:var(--blue);font-size:13px;font-weight:600;padding:6px 20px;background:var(--white)}

/* about */
.about-text{left:100px;top:648px;width:1000px;text-align:center;font-size:12.5px;line-height:23px;color:var(--muted)}
.about-btn{left:540px;top:738px}

/* features */
.features{left:0;top:804px;width:1200px;height:407px;background:var(--light)}
.feature{position:absolute;top:50px;width:240px;text-align:center}
.feature .icon{width:112px;height:112px;border-radius:50%;background:var(--blue);margin:0 auto;display:flex;align-items:center;justify-content:center}
.feature h3{font-size:17px;font-weight:600;color:var(--ink);margin-top:24px}
.feature p{font-size:12.5px;line-height:23px;color:var(--muted);margin-top:22px}
.feature .btn{margin-top:20px}

/* products */
.products{left:0;top:1211px;width:1200px;height:564px;background:linear-gradient(135deg,#3a3a3a,#5a5a5a 50%,#2f2f2f)}
.products .title{color:var(--white);top:48px}
.card{position:absolute;top:135px;width:240px;height:362px}
.card .half{position:absolute;left:0;width:240px;height:181px}
.card .photo{background:linear-gradient(135deg,#8c8c8c,#c9c9c9)}
.card .photo.warm{background:linear-gradient(135deg,#6b5a8a,#d8a76a 60%,#5aa0c8)}
.card .pane{padding:18px 14px;text-align:center}
.pane.white{background:var(--white);color:var(--muted)}
.pane.blue{background:var(--blue);color:var(--white)}
.pane h3{font-size:17px;font-weight:600;margin-bottom:10px}
.pane.white h3{color:var(--ink)}
.pane p{font-size:12px;line-height:20px}
.pane .btn{margin-top:14px;padding:4px 18px;font-size:12.5px}
.pane.blue .btn{background:transparent;border-color:var(--white);color:var(--white)}

/* why choose */
.why{left:0;top:1775px;width:600px;height:357px;background:var(--light)}
.why h2{position:absolute;left:100px;top:40px;font-size:24px;font-weight:600;color:var(--ink)}
.why h2 b{color:var(--blue);font-weight:600}
.why p{position:absolute;left:100px;top:100px;width:460px;font-size:12.5px;line-height:22px;color:var(--text)}
.perk{position:absolute;display:flex;align-items:center;gap:12px;font-family:"Montserrat",sans-serif;font-size:13px;font-weight:600;color:var(--ink)}
.perk i{width:40px;height:40px;border-radius:50%;background:var(--blue);display:flex;align-items:center;justify-content:center}
.why-photo{left:600px;top:1775px;width:600px;height:357px;background:linear-gradient(120deg,#d9dcdf,#b7bcc2 55%,#8a8e96)}

/* testimonials */
.quote{left:200px;top:2248px;width:800px;text-align:center;font-style:italic;font-size:13px;line-height:23px;color:var(--text)}
.arrow{position:absolute;top:2268px}
.author{position:absolute;left:476px;top:2346px;display:flex;align-items:center}
.author .qmark{width:64px;height:64px;border-radius:50%;background:var(--blue);display:flex;align-items:center;justify-content:center;position:relative;z-index:1}
.author .avatar{width:80px;height:80px;border-radius:50%;background:linear-gradient(135deg,#c9a98a,#7a6a5a);border:4px solid var(--white);box-shadow:0 0 0 1px #ccc;margin-left:-16px}
.author .who{margin-left:16px;font-family:"Montserrat",sans-serif}
.author .who strong{display:block;font-size:18px;color:var(--blue);font-weight:600}
.author .who span{font-size:13px;color:var(--muted)}

/* support band */
.support{left:0;top:2479px;width:1200px;height:163px;background:linear-gradient(180deg,#6ea92c,#4f8a1a)}
.support h2{position:absolute;left:0;width:1200px;top:34px;text-align:center;font-family:"Open Sans",sans-serif;font-style:italic;font-weight:700;font-size:26px;color:var(--white)}
.channel{position:absolute;top:94px;display:flex;gap:14px;align-items:flex-start;color:var(--white)}
.channel strong{display:block;font-style:italic;font-weight:600;font-size:18px;line-height:20px}
.channel span{font-style:italic;font-size:13px;opacity:.9}

/* footer */
.footer{left:0;top:2642px;width:1200px;height:69px;background:var(--footer);color:var(--white);font-family:"Montserrat",sans-serif;font-size:13px;font-weight:600}
.footer .links{position:absolute;left:98px;top:26px}
.footer .social{left:624px;top:28px}
.footer .copy{position:absolute;right:98px;top:27px;font-size:12px}
</style>
</head>
<body>

<div class="abs topbar">
  <div class="social"><span></span><span></span><span></span><span></span><span></span></div>
  <div class="contact-top">
    <span><svg width="16" height="12" viewBox="0 0 16 12"><rect x="0.5" y="0.5" width="15" height="11" fill="none" stroke="#fff"/><path d="M1 1l7 6 7-6" fill="none" stroke="#fff"/></svg>info@tallowbanners.com</span>
    <span><svg width="14" height="14" viewBox="0 0 24 24"><path fill="#fff" d="M6.6 10.8a15 15 0 006.6 6.6l2.2-2.2a1 1 0 011-.25 11.4 11.4 0 003.6.57 1 1 0 011 1V20a1 1 0 01-1 1A17 17 0 013 4a1 1 0 011-1h3.5a1 1 0 011 1c0 1.25.2 2.45.57 3.57a1 1 0 01-.25 1z"/></svg>123-456-7890</span>
  </div>
</div>

<header class="abs header">
  <div class="brand"><i></i>Tallow Banners</div>
  <nav class="nav">
    <a class="active">Home</a><a>About Us</a><a>Product</a><a>Category</a><a>FAQ's</a><a>Contact Us</a>
  </nav>
</header>

<section class="abs hero" role="img" aria-label="Workshop floor with printed banners laid out for packing">
  <h1>We Are A New Australian Firm Which Will Sell Large Format Printed Banners And Other Signage Material</h1>
  <span class="btn-yellow">CONACT NOW !</span>
  <div class="circ" role="img" aria-label="Person holding a printed banner" style="left:664px;top:8px;width:216px;height:216px;background:linear-gradient(135deg,#4a6a7a,#c8b8a0)"></div>
  <div class="circ" role="img" aria-label="Stack of printed retail signs" style="left:882px;top:8px;width:216px;height:216px;background:linear-gradient(135deg,#e8e8ee,#3a6ab8)"></div>
  <div class="circ" role="img" aria-label="Row of colourful hanging flag banners" style="left:664px;top:202px;width:216px;height:216px;background:linear-gradient(135deg,#c23a2a,#e8c040 50%,#2a6a3a)"></div>
  <div class="circ" role="img" aria-label="Large printed banner on a building" style="left:882px;top:202px;width:216px;height:216px;background:linear-gradient(135deg,#b82a2a,#e8d8c0)"></div>
  <div class="hero-brand">Tallow<br>Banners</div>
  <div class="dots"><span></span><span class="on"></span><span></span><span></span></div>
</section>

<h2 class="title" style="top:578px">ABOUT <b>TALLOW</b> BANNERS</h2>
<div class="rule" style="top:624px"></div>
<p class="abs about-text">Lorem ipsum dolor sit amet, consectetur adipiscing elit. Aenean et dignissim sem, interdum risus. Vestibulum consectetur nisi mollis diam pulvinar adipiscing. Vestibulum ut urna nec nibh adipiscing facilisis. Etiam auctor porta lacus ac luctus. Praesent ac libero fermentum, rhoncus magna a, dapibus mauris. Nam ut auctor justo. Sed ante odio, luctus quis nequ nec, adipiscing eleifend arcu. Integer nunc turpis, porttitor at lorem ut.Quisque hendrerit</p>
<a class="abs btn about-btn">READ MORE</a>

<section class="abs features">
  <div class="feature" style="left:93px">
    <div class="icon"><svg width="44" height="44" viewBox="0 0 24 24"><path d="M4 12l5 5L20 6" fill="none" stroke="#fff" stroke-width="3"/></svg></div>
    <h3>Quality Printing</h3>
    <p>Lorem ipsum dolor sit amet, consectetur adipiscing elit. Aenean et dignissim sem, interdum risus.</p>
    <a class="btn">READ MORE</a>
  </div>
  <div class="feature" style="left:350px">
    <div class="icon"><svg width="46" height="46" viewBox="0 0 24 24"><circle cx="12" cy="13" r="8" fill="none" stroke="#fff" stroke-width="2.2"/><path d="M12 9v4l3 2M10 2h4" fill="none" stroke="#fff" stroke-width="2.2"/></svg></div>
    <h3>Timely Delivery</h3>
    <p>Lorem ipsum dolor sit amet, consectetur adipiscing elit. Aenean et dignissim sem, interdum risus.</p>
    <a class="btn">READ MORE</a>
  </div>
  <div class="feature" style="left:606px">
    <div class="icon"><svg width="46" height="46" viewBox="0 0 24 24"><circle cx="12" cy="12" r="9" fill="none" stroke="#fff" stroke-width="2.2"/><path d="M7 15c3 0 7-3 8-8M7 15c0-4 3-7 8-8" fill="none" stroke="#fff" stroke-width="2"/></svg></div>
    <h3>Eco-Minded</h3>
    <p>Lorem ipsum dolor sit amet, consectetur adipiscing elit. Aenean et dignissim sem, interdum risus.</p>
    <a class="btn">READ MORE</a>
  </div>
  <div class="feature" style="left:867px">
    <div class="icon"><svg width="46" height="46" viewBox="0 0 24 24"><rect x="4" y="6" width="16" height="12" rx="2" fill="none" stroke="#fff" stroke-width="2.2"/><circle cx="12" cy="12" r="2.5" fill="#fff"/></svg></div>
    <h3>Money Back Guaranteed</h3>
    <p>Lorem ipsum dolor sit amet, consectetur adipiscing elit. Aenean et dignissim sem, interdum risus.</p>
    <a class="btn">READ MORE</a>
  </div>
</section>

<section class="abs products" role="img" aria-label="Dimmed close-up of printed stickers and signage">
  <h2 class="title">PRODUCT CATEGORIES</h2>
  <div class="card" style="left:98px">
    <div class="half photo" style="top:0" role="img" aria-label="Large format printer cutting table"></div>
    <div class="half pane white" style="top:181px"><h3>Lorem ipsum dolor sit</h3><p>Lorem ipsum dolor sit amet, consectetur adipiscing elit. Aenean et dignissim sem, interdum risus.</p><a class="btn">READ MORE</a></div>
  </div>
  <div class="card" style="left:352px">
    <div class="half pane blue" style="top:0"><h3>Lorem ipsum dolor sit</h3><p>Lorem ipsum dolor sit amet, consectetur adipiscing elit. Aenean et dignissim sem, interdum risus.</p><a class="btn">READ MORE</a></div>
    <div class="half photo warm" style="top:181px" role="img" aria-label="Wide printer producing a colourful print"></div>
  </div>
  <div class="card" style="left:607px">
    <div class="half photo warm" style="top:0" role="img" aria-label="Illuminated display panels in a shopping centre"></div>
    <div class="half pane white" style="top:181px"><h3>Lorem ipsum dolor sit</h3><p>Lorem ipsum dolor sit amet, consectetur adipiscing elit. Aenean et dignissim sem, interdum risus.</p><a class="btn">READ MORE</a></div>
  </div>
  <div class="card" style="left:862px">
    <div class="half pane blue" style="top:0"><h3>Lorem ipsum dolor sit</h3><p>Lorem ipsum dolor sit amet, consectetur adipiscing elit. Aenean et dignissim sem, interdum risus.</p><a class="btn">READ MORE</a></div>
    <div class="half photo warm" style="top:181px" role="img" aria-label="Printed vinyl rolls coming off a press"></div>
  </div>
</section>

<section class="abs why">
  <h2>WHY CHOOSE <b>TALLOW</b> BANNERS</h2>
  <p>Lorem ipsum dolor sit amet, consectetur adipiscing elit. Aenean et dignissim sem, interdum risus. Vestibulum consectetur nisi mollis diam pulvinar adipisc Vestibulum ut urna nec nibh adipiscing facilisis Lorem ipsum dolor sit amet, consectetur adipiscing elit.</p>
  <div class="perk" style="left:98px;top:205px"><i><svg width="20" height="20" viewBox="0 0 24 24"><circle cx="12" cy="10" r="6" fill="none" stroke="#fff" stroke-width="2.2"/><path d="M8 15l-2 7 6-3 6 3-2-7" fill="none" stroke="#fff" stroke-width="2"/></svg></i>100% Quality Guarantee</div>
  <div class="perk" style="left:358px;top:205px"><i><svg width="20" height="20" viewBox="0 0 24 24"><circle cx="12" cy="12" r="9" fill="none" stroke="#fff" stroke-width="2"/><path d="M15 8h-4a2 2 0 000 4h2a2 2 0 010 4H9M12 6v12" fill="none" stroke="#fff" stroke-width="2"/></svg></i>Best Price Guarantee</div>
  <div class="perk" style="left:98px;top:266px"><i><svg width="22" height="20" viewBox="0 0 24 20"><rect x="1" y="4" width="14" height="10" fill="#fff"/><path d="M15 7h5l3 4v3h-8z" fill="#fff"/><circle cx="6" cy="16" r="2" fill="#fff"/><circle cx="19" cy="16" r="2" fill="#fff"/></svg></i>Free Shipping</div>
  <div class="perk" style="left:358px;top:266px"><i><svg width="20" height="20" viewBox="0 0 24 24"><rect x="3" y="4" width="18" height="13" fill="none" stroke="#fff" stroke-width="2"/><path d="M8 21h8M7 13l4-4 3 3" fill="none" stroke="#fff" stroke-width="2"/></svg></i>Free Design Proofs</div>
</section>
<div class="abs why-photo" role="img" aria-label="Print technician operating a large office printer"></div>

<h2 class="title" style="top:2172px">WHAT OUR CLIENTS SAY</h2>
<div class="rule" style="top:2216px;left:380px;width:440px"></div>
<svg class="arrow" style="left:98px" width="30" height="58" viewBox="0 0 30 58"><path d="M28 2L3 29l25 27" fill="none" stroke="#555" stroke-width="1.5"/></svg>
<svg class="arrow" style="left:1072px" width="30" height="58" viewBox="0 0 30 58"><path d="M2 2l25 27L2 56" fill="none" stroke="#555" stroke-width="1.5"/></svg>
<p class="abs quote">Lorem ipsum dolor sit amet, consectetuer adipiscing elit, sed diam nonummy nibh euismod tincidunt ut laoreet dolore magna aliquam erat volutpat. Ut wisi enim minim veniam, quis nostrud exerci tation ullamcorper suscipit lobortis nisl ut aliquip ex ea commodo consequat. Ut wisi enim minim veniam, quis nostrud exerci tation ullamcorper suscipit lobortis nisl ut aliquip ex ea commodo consequat.</p>
<div class="author">
  <div class="qmark"><svg width="30" height="26" viewBox="0 0 30 26"><path d="M2 26V14C2 6 6 2 13 1v5c-4 1-5 3-5 7h5v13zM17 26V14c0-8 4-12 11-13v5c-4 1-5 3-5 7h5v13z" fill="#fff"/></svg></div>
  <div class="avatar" role="img" aria-label="Client portrait"></div>
  <div class="who"><strong>Owen Carrick</strong><span>Lorem Ipsum</span></div>
</div>

<section class="abs support" role="img" aria-label="Green textured band">
  <h2>We're Dedicated to Our Customers 24x7</h2>
  <div class="channel" style="left:98px"><svg width="38" height="38" viewBox="0 0 24 24"><path fill="#fff" d="M6.6 10.8a15 15 0 006.6 6.6l2.2-2.2a1 1 0 011-.25 11.4 11.4 0 003.6.57 1 1 0 011 1V20a1 1 0 01-1 1A17 17 0 013 4a1 1 0 011-1h3.5a1 1 0 011 1c0 1.25.2 2.45.57 3.57a1 1 0 01-.25 1z"/></svg><div><strong>123-456-7890</strong><span>Available 24/7 - Call us any time.</span></div></div>
  <div class="channel" style="left:418px"><svg width="44" height="34" viewBox="0 0 44 34"><rect x="1.5" y="1.5" width="41" height="31" fill="none" stroke="#fff" stroke-width="3"/><path d="M2 2l20 17L42 2M2 32l15-14M42 32L27 18" fill="none" stroke="#fff" stroke-width="3"/></svg><div><strong>Email Us</strong><span>Have a question? Let us help.</span></div></div>
  <div class="channel" style="left:726px"><svg width="44" height="36" viewBox="0 0 44 36"><ellipse cx="22" cy="15" rx="19" ry="12" fill="none" stroke="#fff" stroke-width="3"/><path d="M12 25l-4 9 10-6" fill="none" stroke="#fff" stroke-width="3"/></svg><div><strong>Live Chat</strong><span>Online Support</span></div></div>
  <div class="channel" style="left:932px"><svg width="26" height="40" viewBox="0 0 26 40"><path d="M3 11a10 10 0 0120 0c0 7-10 8-10 16" fill="none" stroke="#fff" stroke-width="4"/><circle cx="13" cy="35" r="3" fill="#fff"/></svg><div><strong>Help</strong><span>Find your answers.</span></div></div>
</section>

<footer class="abs footer">
  <div class="links">Home &nbsp;/&nbsp; About Us &nbsp;/&nbsp; Product &nbsp;/&nbsp; Category &nbsp;/&nbsp; FAQ's &nbsp;/&nbsp; Contact Us</div>
  <div class="social"><span></span><span></span><span></span><span></span><span></span></div>
  <div class="copy">© 2016 TALLOW BANNERS. ALL RIGHTS RESERVED.</div>
</footer>

</body>
</html>
```